Leaflet to promote a new sports massage business

I am a Remedial and Sports Massage therapist and treat a range of people from professionals who spend hours working behind computers and have associated neck and back pain through poor posture to amateur sports people of varying intensity/ability - who encounter injuries along the way, or just need some good old stretching out.Remedial and sports massage helps people who have musculoskeletal injury, pain or dysfunction brought about by the stresses and strains of life. Through massage i can reduce pain, promote recovery after injury, relieve stress, and improve flexibility. All of this contributes to helping people feel better. I have just started working at a new location (address attached) and am looking to raise awareness that I am there and to promote the benefits of massage to encourage new clients(attached as a separate document). I have a business card (attached to the brief) which uses hands as the main device, I would like to include these – possibly in some sort of logo and I would like to use purple as a key colour (if colour is used). I also want to include the KVTB logo (attached) to add credibility

```html
<!DOCTYPE html>
<html lang="en">
<head>
<meta charset="utf-8">
<title>Remedial and Sports Massage Leaflet</title>
<link rel="stylesheet" href="https://fonts.googleapis.com/css2?family=Jost:wght@400;500;600&display=swap">
<style>
  :root {
    --plum-deep: #4a1a4e;
    --plum: #8e3d8c;
    --plum-soft: #c890c0;
    --lilac: #9a4fa8;
    --blush: #f1dcec;
    --blush-light: #faf1f8;
    --hands-a: #7a3478;
    --hands-b: #b06aaa;
    --photo-a: #c9d2da;
    --photo-b: #7c93a8;
    --white: #ffffff;
    --page: #ffffff;
  }
  * { margin: 0; padding: 0; box-sizing: border-box; }
  html, body { width: 1200px; height: 1000px; overflow: hidden; background: var(--page); }
  body { font-family: "Jost", "Futura", sans-serif; position: relative; }

  .leaflet {
    position: absolute; left: 255px; top: 12px;
    width: 690px; height: 976px;
    overflow: hidden;
    border: 1px solid #d8d8d8;
    box-shadow: 0 1px 4px rgba(0,0,0,0.15);
  }
  .leaflet-art { position: absolute; inset: 0; }

  .headline {
    position: absolute; left: 246px; top: 42px; width: 410px;
    text-align: center; color: var(--white); font-weight: 500; line-height: 1;
    text-shadow: 0 2px 4px rgba(60,10,60,0.35);
  }
  .headline .main { display: block; font-size: 70px; letter-spacing: 1px; }
  .headline .joiner { display: block; font-size: 30px; margin-top: 8px; }
  .headline .sub { display: block; font-size: 40px; margin-top: 4px; }

  .accreditation {
    position: absolute; left: 18px; top: 528px; width: 134px; height: 134px;
    display: flex; align-items: center; justify-content: center; gap: 8px;
    color: var(--plum-deep); font-size: 24px; font-weight: 500;
  }
  .accreditation .dot { width: 14px; height: 14px; border-radius: 50%; background: var(--lilac); }

  .benefits { position: absolute; left: 0; top: 642px; width: 690px; text-align: center; }
  .benefits h2 { font-size: 29px; font-weight: 500; line-height: 40px; color: var(--plum-deep); letter-spacing: 0.3px; }
  .benefits ul { list-style: none; }
  .benefits li { font-size: 18px; font-weight: 500; line-height: 23px; color: var(--plum-deep); }
  .benefits li:nth-child(even) { color: var(--lilac); }
  .benefits li::before {
    content: ""; display: inline-block; width: 8px; height: 8px; border-radius: 50%;
    background: var(--plum); margin-right: 6px; vertical-align: 2px;
    box-shadow: inset 0 0 0 1.5px #d7a9d2;
  }

  .contact { position: absolute; left: 0; top: 830px; width: 690px; text-align: center; color: var(--plum-deep); }
  .contact .name { font-size: 19px; font-weight: 600; line-height: 27px; }
  .contact .role { font-size: 21px; color: var(--lilac); line-height: 26px; }
  .contact .line { font-size: 17px; line-height: 21px; display: flex; justify-content: center; align-items: center; gap: 6px; }
  .contact .line svg { width: 18px; height: 14px; }
  .contact .square { width: 16px; height: 16px; background: var(--plum); display: inline-block; }
</style>
</head>
<body>
<main class="leaflet">
  <svg class="leaflet-art" viewBox="0 0 690 976" width="690" height="976">
    <defs>
      <linearGradient id="headerFill" x1="0" y1="0" x2="1" y2="1">
        <stop offset="0" stop-color="#c37fbd"/>
        <stop offset="0.5" stop-color="#a45aa0"/>
        <stop offset="1" stop-color="#8e3d8c"/>
      </linearGradient>
      <linearGradient id="handsFill" x1="0" y1="0" x2="1" y2="1">
        <stop offset="0" stop-color="var(--hands-a)"/>
        <stop offset="1" stop-color="var(--hands-b)" stop-opacity="0.6"/>
      </linearGradient>
      <linearGradient id="photoFill" x1="0" y1="0" x2="1" y2="1">
        <stop offset="0" stop-color="var(--photo-a)"/>
        <stop offset="0.55" stop-color="#5e9bc9"/>
        <stop offset="1" stop-color="var(--photo-b)"/>
      </linearGradient>
      <linearGradient id="lowerFill" x1="0" y1="0" x2="0" y2="1">
        <stop offset="0" stop-color="#f3d6ec"/>
        <stop offset="1" stop-color="#fbf6fa"/>
      </linearGradient>
    </defs>

    <rect class="lower-panel" width="690" height="976" fill="url(#lowerFill)"/>
    <path class="wave" d="M0,420 C120,560 260,640 420,640 C540,640 620,600 690,560 V620 C560,690 380,700 250,680 C140,660 60,600 0,560 Z" fill="#e7b9dc" opacity="0.6"/>
    <path class="wave" d="M0,740 C200,760 460,700 690,640 V720 C470,780 220,810 0,800 Z" fill="#ecc4e3" opacity="0.55"/>
    <path class="wave" d="M0,810 C240,840 480,780 690,760 V800 C470,830 240,870 0,860 Z" fill="#ffffff" opacity="0.5"/>

    <path class="photo" role="img" aria-label="Photo of a therapist massaging the shoulder of a woman lying on her side on a treatment mat"
      d="M0,200 C200,215 450,205 690,175 V520 C600,565 480,615 340,622 C200,625 90,520 0,400 Z" fill="url(#photoFill)"/>

    <path class="header" d="M0,0 H690 V172 C560,212 350,240 0,236 Z" fill="url(#headerFill)"/>
    <path class="header-band" d="M0,236 C350,240 560,212 690,172 V190 C560,230 350,254 0,246 Z" fill="#e9bfe0"/>

    <rect class="hands-art" role="img" aria-label="Illustration of two overlapping open hands in deep purple"
      x="0" y="0" width="235" height="213" fill="url(#handsFill)"/>

    <circle class="seal" cx="85" cy="595" r="76" fill="#f0d3ea"/>
    <circle class="seal-inner" cx="85" cy="595" r="68" fill="var(--white)"/>
  </svg>

  <h1 class="headline">
    <span class="main">REMEDIAL</span>
    <span class="joiner">AND</span>
    <span class="sub">SPORTS MASSAGE</span>
  </h1>

  <div class="accreditation"><span class="dot"></span>KVTB</div>

  <section class="benefits">
    <h2>BENEFITS OF MASSAGE</h2>
    <ul>
      <li>Reduces Pain</li>
      <li>Promotes Recovery</li>
      <li>Improves Posture And Flexibility</li>
      <li>Relieves Stress</li>
      <li>Improves Health And Wellbeing</li>
    </ul>
  </section>

  <section class="contact">
    <p class="name">Rosa Marchetti</p>
    <p class="role">Remedial and Sports Massage Therapist</p>
    <p class="line">
      <svg viewBox="0 0 18 14"><path d="M2,5 C5,1 13,1 16,5 L14,7 L12,5 L6,5 L4,7 Z M5,7 H13 L15,13 H3 Z" fill="var(--plum-deep)"/></svg>
      07700 900418
    </p>
    <p class="line">
      <svg viewBox="0 0 18 14"><rect x="1" y="1" width="16" height="12" fill="var(--plum)"/><path d="M1,1 L9,8 L17,1" stroke="#fff" stroke-width="1.4" fill="none"/></svg>
      rosamarchetti@mailpost.com
    </p>
    <p class="line"><span class="square"></span>socialpage.com/RosaMarchettiMassage</p>
  </section>
</main>
</body>
</html>
```